Newsletter template

I am looking for 2 newsletter templates. My website is in Wordpress and I want to use in mailchimp for lists.

One newsletter is for local clients of design remodeling firm to be sent monthly

Second newsletter is for web store offerings to be sent weekly.

Target Market(s)

Luxury home and leisure

Industry/Entity Type

Store

Requirements
Must have
• Use logos and colors to seamlessly integrate with website,

```html
<!DOCTYPE html>
<html lang="en">
<head>
<meta charset="utf-8">
<title>Maren Lowe – Weekly Offers</title>
<link rel="stylesheet" href="https://fonts.googleapis.com/css2?family=Roboto+Condensed:wght@400;700&family=Arimo:wght@400;700&family=Parisienne&display=swap">
<style>
  :root{
    --teal:#00a3c4;
    --teal-dark:#0090ad;
    --lime:#dde000;
    --orange:#e8562a;
    --green:#22cc00;
    --ink:#1f1f1f;
    --grey-line:#cfcfcf;
    --muted:#555;
    --white:#ffffff;
  }
  *{box-sizing:border-box;margin:0;padding:0}
  html,body{width:1200px;height:2182px;overflow:hidden;background:var(--white)}
  body{position:relative;font-family:"Arimo",Arial,sans-serif;color:var(--ink)}
  .abs{position:absolute}
  .cond{font-family:"Roboto Condensed","Arial Narrow",sans-serif}

  .preheader{top:22px;left:0;width:1200px;text-align:center;font-size:14px;color:#222}
  .preheader a{color:var(--teal)}

  .welcome{top:62px;left:119px;width:959px;height:102px;background:var(--teal)}
  .welcome-inner{position:absolute;inset:13px;border:1px solid rgba(255,255,255,.6);
    display:flex;align-items:center;justify-content:center;color:var(--white);
    font-size:34px}

  .brand{top:186px;left:119px;font-size:56px;color:var(--teal);line-height:1;display:flex;align-items:center;gap:14px}
  .brand-dot{width:18px;height:18px;border-radius:50%;background:var(--lime)}

  .account-btn{top:211px;height:36px;background:var(--teal);color:var(--white);border-radius:3px;
    font-size:17px;display:flex;align-items:center;justify-content:center}
  .account-login{left:869px;width:99px}
  .account-register{left:978px;width:100px}

  .hero{top:288px;left:119px;width:959px;height:456px;
    background:linear-gradient(100deg,#e9ecef 0%,#c9d2da 35%,#aab8c6 55%,#d7dde3 75%,#c9ad87 100%)}
  .hero-title{top:154px;left:77px;font-size:53px;line-height:58px;color:var(--ink);font-weight:400}
  .hero-sub{top:282px;left:77px;font-size:35px;color:var(--teal)}
  .hero-btn{top:344px;left:77px;width:353px;height:71px;background:var(--teal);padding:7px}
  .hero-btn span{display:flex;width:100%;height:100%;border:2px solid var(--white);align-items:center;justify-content:center;
    color:var(--white);font-size:27px;font-family:"Arimo",Arial,sans-serif}

  .tile{top:770px;height:280px;border:1px solid var(--grey-line);padding:4px}
  .tile-img{position:relative;width:100%;height:100%}
  .tile-1{left:119px;width:302px}
  .tile-1 .tile-img{background:linear-gradient(135deg,#d8c79a 0%,#6d86c9 45%,#4d6cc0 100%)}
  .tile-2{left:443px;width:301px}
  .tile-2 .tile-img{background:linear-gradient(160deg,#6b4a5e 0%,#b49aa6 45%,#e6dde0 100%)}
  .tile-3{left:777px;width:301px}
  .tile-3 .tile-img{background:linear-gradient(150deg,#8a8a86 0%,#4a4a48 50%,#2f2f2e 100%)}
  .tile-text{position:absolute;font-size:28px;line-height:33px}
  .tile-1 .tile-text{top:135px;left:20px;color:var(--ink)}
  .tag-pop{position:absolute;top:173px;left:22px;width:229px;height:40px;background:var(--green);color:var(--white);
    font-size:25px;display:flex;align-items:center;justify-content:center}
  .tile-cta{position:absolute;top:226px;left:20px;color:var(--orange);font-size:23px}
  .tile-2 .tile-text{top:180px;left:18px;color:var(--ink)}
  .tile-3 .tile-text{top:152px;left:20px;color:var(--white);font-weight:700}

  .product{height:193px;border:1px solid var(--grey-line)}
  .col-a{left:119px;width:467px}
  .col-b{left:612px;width:466px}
  .row-1{top:1100px}
  .row-2{top:1322px}
  .row-3{top:1540px}
  .product-img{position:absolute;left:18px;top:20px;width:162px;height:150px}
  .product-name{position:absolute;left:203px;top:32px;color:var(--teal);font-size:27px;line-height:33px;width:200px}
  .product-name small{font-size:17px}
  .product-price{position:absolute;left:203px;top:110px;color:var(--orange);font-size:29px}
  .order-btn{position:absolute;left:308px;top:119px;width:140px;height:36px;background:var(--lime);color:var(--white);
    font-size:19px;display:flex;align-items:center;justify-content:center}
  .badge{position:absolute;left:358px;top:-8px;width:110px;height:110px}
  .badge-text{position:absolute;left:358px;top:24px;width:110px;text-align:center;color:var(--white);font-size:19px;line-height:23px}

  .about{top:1764px;left:119px;width:959px;height:293px;background:var(--teal)}
  .about-inner{position:absolute;inset:13px;border:1px solid rgba(255,255,255,.55)}
  .about-title{position:absolute;top:30px;left:0;width:100%;text-align:center;color:var(--white);font-size:35px}
  .about-brand{position:absolute;top:120px;left:38px;font-size:64px;color:var(--white);line-height:1}
  .about-divider{position:absolute;left:446px;top:108px;width:2px;height:138px;background:rgba(255,255,255,.8)}
  .about-copy{position:absolute;left:492px;top:104px;width:420px;color:var(--white);font-size:14px;line-height:29.5px}

  .footer-note{top:2104px;left:123px;font-size:14px;color:var(--muted)}
  .social{top:2094px;width:38px;height:38px;border-radius:50%}
</style>
</head>
<body>

  <p class="abs preheader">If you are not able to view this mailer properly, please <a href="#">click here</a></p>

  <div class="abs welcome"><div class="welcome-inner cond">Hello! Welcome to our shop. Check our current offers.</div></div>

  <div class="abs brand cond"><span class="brand-dot"></span>Maren Lowe</div>
  <a class="abs account-btn account-login">Login</a>
  <a class="abs account-btn account-register">Register</a>

  <section class="abs hero" role="img" aria-label="Photo of a bedroom with a tufted grey headboard, patterned pillows and bedside lamps">
    <h1 class="abs hero-title cond">SAVE 10% ON<br>ALL GRAB BARS</h1>
    <p class="abs hero-sub cond">THIS MONTH ONLY</p>
    <a class="abs hero-btn"><span>Teak Collections</span></a>
  </section>

  <div class="abs tile tile-1">
    <div class="tile-img" role="img" aria-label="Photo of blue embroidered garden cushions">
      <p class="tile-text cond">GARDEN STYLE</p>
      <p class="tag-pop cond">FOR A POP OF COLOR!</p>
      <p class="tile-cta cond">CHECK IT NOW</p>
    </div>
  </div>
  <div class="abs tile tile-2">
    <div class="tile-img" role="img" aria-label="Photo of a teapot with pink roses on a table">
      <p class="tile-text cond">AUTHENTIC ACCENTS<br>FOR YOUR HOME</p>
    </div>
  </div>
  <div class="abs tile tile-3">
    <div class="tile-img" role="img" aria-label="Photo of a weathered stone garden statue">
      <p class="tile-text cond">CHECK OUT<br>GARDEN STATUARY<br>AND ACCENTS</p>
    </div>
  </div>

  <!-- product grid -->
  <article class="abs product col-a row-1">
    <div class="product-img" role="img" aria-label="Silver oil and vinegar cruet stand" style="background:linear-gradient(180deg,#f3f3f3,#bdbdbd)"></div>
    <h2 class="product-name cond">Olive Oil and<br>Vinegar</h2>
    <p class="product-price cond">$80.00</p>
    <a class="order-btn cond">Order Now</a>
    <svg class="badge" viewBox="0 0 110 110"><circle cx="55" cy="55" r="48" fill="var(--orange)" stroke="var(--orange)" stroke-width="7" stroke-dasharray="2 4" stroke-linecap="round"/></svg>
    <p class="badge-text cond">New on<br>Sale</p>
  </article>

  <article class="abs product col-b row-1">
    <div class="product-img" role="img" aria-label="Pair of silver starfish ornaments" style="background:linear-gradient(180deg,#f4f4f4,#c4c4c4)"></div>
    <h2 class="product-name cond">PAINTED<br>WATERING CAN</h2>
    <p class="product-price cond">$80.00</p>
    <a class="order-btn cond">Order Now</a>
    <svg class="badge" viewBox="0 0 110 110"><circle cx="55" cy="55" r="48" fill="var(--orange)" stroke="var(--orange)" stroke-width="7" stroke-dasharray="2 4" stroke-linecap="round"/></svg>
    <p class="badge-text cond">New on<br>Sale</p>
  </article>

  <article class="abs product col-a row-2">
    <div class="product-img" role="img" aria-label="Silver sculptural candelabra" style="background:linear-gradient(180deg,#f2f2f2,#b3b3b3)"></div>
    <h2 class="product-name cond">Towel Bar <small>with<br>Integrated Support Rail 24</small></h2>
    <p class="product-price cond">$80.00</p>
    <a class="order-btn cond">Order Now</a>
    <svg class="badge" viewBox="0 0 110 110"><circle cx="55" cy="55" r="48" fill="var(--orange)" stroke="var(--orange)" stroke-width="7" stroke-dasharray="2 4" stroke-linecap="round"/></svg>
    <p class="badge-text cond">New on<br>Sale</p>
  </article>

  <article class="abs product col-b row-2">
    <div class="product-img" role="img" aria-label="Red metal watering can" style="background:linear-gradient(180deg,#f1e4e2,#c8463a)"></div>
    <h2 class="product-name cond">Unique Touch<br>Robe Hook</h2>
    <p class="product-price cond">$80.00</p>
    <a class="order-btn cond">Order Now</a>
    <svg class="badge" viewBox="0 0 110 110"><circle cx="55" cy="55" r="48" fill="var(--orange)" stroke="var(--orange)" stroke-width="7" stroke-dasharray="2 4" stroke-linecap="round"/></svg>
    <p class="badge-text cond">New on<br>Sale</p>
  </article>

  <article class="abs product col-a row-3">
    <div class="product-img" role="img" aria-label="Stacks of folded colourful towels" style="background:linear-gradient(180deg,#d9b38a,#c9584a 40%,#3f6fb5 70%,#e5c93a)"></div>
    <h2 class="product-name cond">UNIQUE TOUCH<br>ROBE HOOK</h2>
    <p class="product-price cond">$80.00</p>
    <a class="order-btn cond">Order Now</a>
    <svg class="badge" viewBox="0 0 110 110"><circle cx="55" cy="55" r="48" fill="var(--orange)" stroke="var(--orange)" stroke-width="7" stroke-dasharray="2 4" stroke-linecap="round"/></svg>
    <p class="badge-text cond">New on<br>Sale</p>
  </article>

  <article class="abs product col-b row-3">
    <div class="product-img" role="img" aria-label="Patterned cushion in mint and charcoal" style="background:linear-gradient(135deg,#a9dcd6,#3a3a3a)"></div>
    <h2 class="product-name cond">Olive Oil and<br>Vinegar</h2>
    <p class="product-price cond">$80.00</p>
    <a class="order-btn cond">Order Now</a>
    <svg class="badge" viewBox="0 0 110 110"><circle cx="55" cy="55" r="48" fill="var(--orange)" stroke="var(--orange)" stroke-width="7" stroke-dasharray="2 4" stroke-linecap="round"/></svg>
    <p class="badge-text cond">New on<br>Sale</p>
  </article>

  <section class="abs about">
    <div class="about-inner">
      <h2 class="about-title cond">About Maren Lowe</h2>
      <p class="about-brand cond">Maren Lowe</p>
      <span class="about-divider"></span>
      <p class="about-copy">It is a long established fact that a reader will be distracted by the readable content of a page when looking at its layout. The point of using Lorem Ipsum is that it has a more-or-less normal distribution of letters, as opposed to using 'Content here, content here', making it look like readable English.</p>
    </div>
  </section>

  <p class="abs footer-note">© 2014 Maren Lowe. All rights reserved</p>
  <span class="abs social" style="left:766px;background:#2d5fa8"></span>
  <span class="abs social" style="left:811px;background:#3aa8e0"></span>
  <span class="abs social" style="left:856px;background:#1b7aa6"></span>
  <span class="abs social" style="left:901px;background:#2b2b2b"></span>
  <span class="abs social" style="left:946px;background:#e0262b"></span>
  <span class="abs social" style="left:992px;background:#f0a023"></span>
  <span class="abs social" style="left:1039px;background:#d8232a"></span>

</body>
</html>
```